Stationery Design Project

Letterhead with logo and address
Envelopes with Logo and address

The target market is start-ups and
small to medium businesses primarly located in China, with less than 20
employees. Please have designers use Yellow and Blue colors and our logo
attached. Looking fr the same format as the business card attached.
Updates

Reason: Designer has been delayed working on web design

Target Market(s)

Start-ups and small to medium size businesses

Industry/Entity Type

Business

Font styles to use
Sans Serif

Requirements
Must have
Nice to have
Should not have

```html
<!DOCTYPE html>
<html lang="en">
<head>
<meta charset="utf-8">
<title>NORVA Stationery</title>
<link href="https://fonts.googleapis.com/css2?family=Montserrat:wght@400;600;700&family=Noto+Sans+SC:wght@400&display=swap" rel="stylesheet">
<style>
  :root {
    --navy: #22386a;
    --navy-soft: #2d4679;
    --gold: #d6a91e;
    --paper: #f3f4f6;
    --stage: #e6e7ea;
    --ink: #22386a;
    --muted: #6d7690;
  }
  * { box-sizing: border-box; margin: 0; padding: 0; }
  html, body { width: 1200px; height: 911px; overflow: hidden; }
  body {
    position: relative;
    background: var(--stage);
    font-family: "Montserrat", sans-serif;
    color: var(--ink);
  }
  .sheet { position: absolute; overflow: hidden; box-shadow: 0 2px 6px rgba(0,0,0,.12); }

  .brand { display: flex; flex-direction: column; align-items: center; gap: 6px; position: relative; }
  .brand-dot { width: 30px; height: 30px; border-radius: 50%; background: var(--gold); }
  .brand-name { font-weight: 700; font-size: 13px; letter-spacing: 5px; color: var(--navy); }
  .on-navy .brand-name { color: #9aa7c6; }

  /* Soft tonal placeholder for the decorative background graphic */
  .cover-graphic {
    position: absolute; inset: 0;
    background: linear-gradient(160deg, var(--navy) 45%, var(--navy-soft) 100%);
  }

  /* Letterhead */
  .letterhead { left: 40px; top: 50px; width: 300px; height: 424px; background: var(--paper); }
  .letterhead .brand { position: absolute; top: 30px; left: 0; right: 0; }
  .letterhead-footer {
    position: absolute; left: 0; right: 0; bottom: 0; height: 30px;
    background: var(--navy); border-top: 3px solid var(--gold);
    color: #fff; font-size: 6.5px; line-height: 1.5; text-align: center; padding-top: 6px;
  }

  /* Folder */
  .folder { left: 370px; top: 50px; width: 300px; height: 424px; background: var(--navy); }
  .folder .brand { position: absolute; top: 48px; left: 0; right: 0; }

  /* Envelope */
  .envelope { left: 700px; top: 50px; width: 460px; height: 220px; background: var(--paper); }
  .envelope-flap { position: absolute; left: 0; right: 0; top: 0; height: 62px; background: var(--navy);
    display: flex; align-items: center; justify-content: center; }
  .envelope-flap .brand-dot { width: 20px; height: 20px; }

  /* Note card */
  .notecard { left: 700px; top: 300px; width: 460px; height: 220px; background: var(--paper); }
  .notecard .brand { position: absolute; left: 36px; top: 120px; flex-direction: row; gap: 10px; }
  .notecard-address { position: absolute; left: 76px; top: 148px; font-size: 7px; line-height: 1.5; color: var(--muted); }
  .notecard-band { position: absolute; right: 0; top: 0; bottom: 0; width: 22px; background: var(--navy); border-left: 4px solid var(--gold); }

  /* Business cards */
  .card { width: 210px; height: 120px; background: var(--paper); }
  .card-back { left: 40px; top: 520px; display: flex; }
  .card-back-panel { width: 74px; background: var(--navy); display: flex; flex-direction: column;
    align-items: center; justify-content: center; gap: 8px; }
  .card-back-panel .brand-name { font-size: 8px; letter-spacing: 3px; color: #c9d1e4; }
  .card-back-panel .brand-dot { width: 22px; height: 22px; }
  .card-back-info { flex: 1; padding: 16px 12px; font-size: 6.5px; line-height: 1.7; color: var(--muted); }
  .card-front { left: 40px; top: 660px; padding: 16px 16px; text-align: right; }
  .card-name { font-weight: 700; font-size: 13px; color: var(--navy); }
  .card-title { font-size: 7.5px; font-weight: 600; color: var(--navy); margin-bottom: 8px; }
  .card-company { font-family: "Noto Sans SC", sans-serif; font-size: 7px; color: var(--navy); }
  .card-contact { font-size: 6.5px; line-height: 1.6; color: var(--muted); margin-top: 6px; }
  .card-front-strip { position: absolute; left: 0; right: 0; bottom: 0; height: 5px; background: var(--navy); border-top: 1.5px solid var(--gold); }

  /* Notebook */
  .notebook { left: 300px; top: 520px; width: 270px; height: 360px; background: var(--navy); }
  .notebook .brand { position: absolute; top: 56px; left: 0; right: 0; }
  .notebook-spine { position: absolute; left: 0; top: 0; bottom: 0; width: 14px;
    background: repeating-linear-gradient(to bottom, #6b6f78 0 3px, transparent 3px 11px); }
</style>
</head>
<body>

<section class="sheet letterhead">
  <div class="brand"><span class="brand-dot"></span><span class="brand-name">NORVA</span></div>
  <footer class="letterhead-footer">
    88 Harbour Road, Jing'an District, Shanghai, China<br>
    T +86 21 5550 0188 · E hello@norvapartners.com · W www.norvapartners.com
  </footer>
</section>

<section class="sheet folder on-navy">
  <div class="cover-graphic" role="img" aria-label="Decorative wave graphic in navy tones"></div>
  <div class="brand"><span class="brand-dot"></span><span class="brand-name">NORVA</span></div>
</section>

<section class="sheet envelope">
  <div class="envelope-flap"><span class="brand-dot"></span></div>
</section>

<section class="sheet notecard">
  <div class="brand"><span class="brand-dot"></span><span class="brand-name">NORVA</span></div>
  <p class="notecard-address">88 Harbour Road, Jing'an<br>Shanghai, China</p>
  <div class="notecard-band"></div>
</section>

<section class="sheet card card-back">
  <div class="card-back-panel"><span class="brand-dot"></span><span class="brand-name">NORVA</span></div>
  <div class="card-back-info">
    88 Harbour Road, Jing'an District<br>Shanghai 200040, China<br>www.norvapartners.com
  </div>
</section>

<section class="sheet card card-front">
  <p class="card-name">Lucas Whitfield</p>
  <p class="card-title">President &amp; CEO</p>
  <p class="card-company">诺瓦商务咨询（上海）有限公司</p>
  <p class="card-contact">M +86 138 0555 0199<br>lucas@norvapartners.com</p>
  <div class="card-front-strip"></div>
</section>

<section class="sheet notebook on-navy">
  <div class="cover-graphic" role="img" aria-label="Decorative wave graphic in navy tones"></div>
  <div class="notebook-spine"></div>
  <div class="brand"><span class="brand-dot"></span><span class="brand-name">NORVA</span></div>
</section>

</body>
</html>
```